TALVENTO needs a Sleek, Professional and Serious Web Design, this web design is aiming to be famous!

Dear Designers,

We need a web design for a new company based on the Internet named "talvento". I have already worked with PX to get my logo and it has been a wonderful experience which I want to repeat. We are kind of work social network, the web page will be mostly used to write comments on businesses around the world to help workers find which company fit the best for them. This website is also here to help people finding work by giving them the tools to make the right research.

For contents inspiration, you could see on the added files a sketch of the website but I am not asking you following it because it was just for giving the contents.

We do not have any example regarding website that we do like because all are coming so generic. We would like a very sleek website, where surfing become very intuitive and ergonomic (Brindlepost is not very ergonomic for example from our point of view). The website must reflect professionalism and seriousness and worker, world connexion.

We will be pleased to accept original designs as long as they fit to our requirements and if it is properly made of course: e.g. web page looking like a newspaper etc.

About colours, we are not decided yet but we are aiming a light orange (pastel style) or dark bluish green. Also, it comes to our attention that a web site mostly realized in grey-scale will be very interesting (touch of colour will be accepted as well if it miss too much dynamism) .

We will give the feedback as soon as possible because we would like to have 5 pages but it will be only very small changes on the next ones. (like adding 4 buttons)

Target Market(s)

Our target is relatively large because it is all people of working age, in numbers we can say a range of people aged from 18 to 45 years.

Industry/Entity Type

Internet

Number of Pages Required

3 page

Font styles to use
Sans Serif

Requirements
Must have
• Elements that must be on the web page are exposed below:
• - company logo ( .ai & .eps files on added files)
• - 4 buttons (Searcher "highlighted" / Advises / Jobs / Solutions)
• - login/account window
• - language button (e.g. a flag)
• - Window companies searcher (the most important, refer to the sketch)
• - classic menu down the page - about us / contact us / conditions / site map / community / politics / publicity / languages / copyright etc.
Nice to have
• We want a professional and serious website.
Should not have
• If you have a doubt, just ask us because nothing are coming to our mind.

```html
<!DOCTYPE html>
<html lang="en">
<head>
<meta charset="utf-8">
<title>Talvento</title>
<link rel="stylesheet" href="https://fonts.googleapis.com/css2?family=Source+Sans+3:wght@300;400;600;700&display=swap">
<style>
  :root {
    --orange: #f9a11b;
    --ink: #333333;
    --nav-ink: #222222;
    --muted: #8a8a8a;
    --line: #cfcfcf;
    --panel-head: #f4f4f4;
    --ad-fill: #e0e0e0;
    --footer-bg: #3b3b3b;
    --footer-ink: #f2f2f2;
    --white: #ffffff;
  }
  * { box-sizing: border-box; margin: 0; padding: 0; }
  html, body { width: 1200px; height: 705px; overflow: hidden; background: var(--white); }
  body { font-family: "Source Sans 3", "Source Sans Pro", sans-serif; color: var(--ink); }
  .page { position: relative; width: 1200px; height: 705px; }

  .site-header {
    position: absolute; top: 0; left: 0; width: 1200px; height: 79px;
    background: #fafafa; box-shadow: 0 1px 4px rgba(0,0,0,0.18); z-index: 2;
  }
  .brand { position: absolute; left: 120px; top: 21px; display: flex; align-items: center; gap: 10px; }
  .brand-dot { width: 24px; height: 24px; border-radius: 50%; background: var(--nav-ink); }
  .brand-name { font-size: 34px; font-weight: 700; color: var(--nav-ink); letter-spacing: 0.5px; line-height: 1; }

  .main-nav {
    position: absolute; right: 406px; top: 33px; display: flex; gap: 16px; white-space: nowrap;
  }
  .main-nav a { font-size: 13.5px; font-weight: 600; color: var(--nav-ink); text-decoration: none; text-transform: uppercase; line-height: 17px; }
  .main-nav a.is-active { color: var(--orange); }

  .language-select {
    position: absolute; left: 813px; top: 23px; width: 129px; height: 37px;
    border: 1px solid #c8c8c8; background: var(--white); border-radius: 2px;
    font-size: 12px; color: var(--nav-ink); padding: 0 10px; line-height: 35px; text-transform: uppercase;
  }
  .language-select svg { position: absolute; right: 10px; top: 15px; }
  .login-button {
    position: absolute; left: 949px; top: 22px; width: 131px; height: 39px;
    background: var(--orange); border-radius: 3px; color: var(--white);
    font-size: 12.5px; text-align: center; line-height: 39px; text-transform: uppercase; white-space: nowrap;
  }

  .hero { position: absolute; top: 79px; left: 0; width: 1200px; height: 513px; }
  .hero-backdrop {
    position: absolute; inset: 0;
    background: radial-gradient(ellipse at 45% 55%, #cfcfcf 0%, #e4e4e4 40%, #f3f3f3 75%, #fafafa 100%);
  }
  .hero-title { position: absolute; left: 120px; top: 76px; font-size: 34px; font-weight: 700; color: var(--ink); line-height: 44px; white-space: nowrap; }
  .benefits { position: absolute; left: 120px; top: 150px; list-style: none; }
  .benefits li { position: relative; padding-left: 38px; height: 74px; font-size: 17px; line-height: 25px; white-space: nowrap; }
  .benefits svg { position: absolute; left: 0; top: 8px; }

  .search-panel {
    position: absolute; left: 549px; top: 128px; width: 316px; height: 256px;
    background: var(--white); border: 1px solid #dcdcdc; box-shadow: 0 6px 8px rgba(0,0,0,0.12);
  }
  .search-panel-title {
    height: 50px; background: var(--panel-head); border-bottom: 1px solid #d6d6d6;
    color: var(--orange); font-size: 24px; font-weight: 400; text-align: center; line-height: 50px; white-space: nowrap;
  }
  .search-field {
    position: absolute; left: 23px; width: 269px; height: 46px;
    border: 2px solid var(--line); border-radius: 2px; background: var(--white);
    font-size: 12.5px; color: var(--muted); padding-left: 14px; line-height: 42px; font-weight: 600; white-space: nowrap;
  }
  .search-button {
    position: absolute; left: 23px; top: 186px; width: 269px; height: 46px;
    background: var(--orange); border-radius: 2px; color: var(--white);
    font-size: 12.5px; font-weight: 600; text-align: center; line-height: 46px;
  }

  .ad-slot {
    position: absolute; left: 912px; top: 42px; width: 168px; height: 423px;
    background: var(--ad-fill); display: flex; align-items: center; justify-content: center;
    text-align: center; color: #8e8e8e; font-size: 27px; font-weight: 300; line-height: 25px;
  }

  .site-footer {
    position: absolute; top: 592px; left: 0; width: 1200px; height: 56px;
    background: var(--footer-bg); display: flex; justify-content: center; align-items: center; gap: 42px;
  }
  .site-footer a { color: var(--footer-ink); font-size: 14.5px; font-weight: 300; text-decoration: none; white-space: nowrap; }
  .copyright { position: absolute; top: 670px; width: 1200px; text-align: center; font-size: 10px; color: var(--ink); }
</style>
</head>
<body>
<div class="page">
  <header class="site-header">
    <div class="brand"><span class="brand-dot"></span><span class="brand-name">TALVENTO</span></div>
    <nav class="main-nav">
      <a href="#" class="is-active">Searcher</a>
      <a href="#">Advises</a>
      <a href="#">Jobs</a>
      <a href="#">Solutions</a>
      <a href="#">About us</a>
    </nav>
    <div class="language-select">Language
      <svg width="9" height="6" viewBox="0 0 9 6"><path d="M1 1l3.5 3.5L8 1" fill="none" stroke="#222" stroke-width="1.6"/></svg>
    </div>
    <div class="login-button">Login account</div>
  </header>

  <section class="hero">
    <div class="hero-backdrop" role="img" aria-label="Soft grey world map with connecting orbit lines"></div>
    <h1 class="hero-title">Why Choose Talvento?</h1>
    <ul class="benefits">
      <li><svg width="26" height="22" viewBox="0 0 26 22"><path d="M2 12l7 7L24 2" fill="none" stroke="#f9a11b" stroke-width="5" stroke-linejoin="round"/></svg>Lorem ipsum dolor sit amet, consectetur adipiscing<br>elit. In vel congue enim. Mauris auctor odales.</li>
      <li><svg width="26" height="22" viewBox="0 0 26 22"><path d="M2 12l7 7L24 2" fill="none" stroke="#f9a11b" stroke-width="5" stroke-linejoin="round"/></svg>Lorem ipsum dolor sit amet, consectetur adipiscing<br>elit. In vel congue enim. Mauris auctor odales.</li>
      <li><svg width="26" height="22" viewBox="0 0 26 22"><path d="M2 12l7 7L24 2" fill="none" stroke="#f9a11b" stroke-width="5" stroke-linejoin="round"/></svg>Lorem ipsum dolor sit amet, consectetur adipiscing<br>elit. In vel congue enim. Mauris auctor odales.</li>
      <li><svg width="26" height="22" viewBox="0 0 26 22"><path d="M2 12l7 7L24 2" fill="none" stroke="#f9a11b" stroke-width="5" stroke-linejoin="round"/></svg>Lorem ipsum dolor sit amet, consectetur adipiscing<br>elit. In vel congue enim. Mauris auctor odales.</li>
    </ul>

    <div class="search-panel">
      <div class="search-panel-title">COMPANIES SEARCHER</div>
      <div class="search-field" style="top:73px">COMPANY NAME / VAT NUMBER</div>
      <div class="search-field" style="top:130px">CITY / POST CODE / COUNTRY</div>
      <div class="search-button">SEARCH NOW</div>
    </div>

    <aside class="ad-slot">ADD<br>HERE</aside>
  </section>

  <footer class="site-footer">
    <a href="#">ABOUT US</a>
    <a href="#">CONTACT US</a>
    <a href="#">COMMUNITY</a>
    <a href="#">PUBLICITY</a>
    <a href="#">CONDITIONS</a>
    <a href="#">POLITICS</a>
    <a href="#">LANGUAGE</a>
  </footer>
  <p class="copyright">COPYRIGHT © 2015 TALVENTO. ALL RIGHTS RESERVED</p>
</div>
</body>
</html>
```